Concert festival poster

Poster invitation for 40th party designed to look like a concert festival. Using the samples attached as a guide, looking for a colorful, creative and eye catching invite.
The event will be held over a weekend at a farm, with music food, friends and drinks.

Target Market(s)

Party guests, friends and family

Industry/Entity Type

Festival

Colors

Designer to choose colors to be used in the design.

Requirements
Must have
• Brellafest- Mark Telford's 40th festival
• Event date- 5-7th October 2018. Main event 6th October 2018 from 3pm-late
• Come anytime over the weekend- food, drinks and fun provided.
• Address is 412 Stony Creek Lane, Marulan NSW
• All welcome, including children
• Bring your own tent or let us know and we can arrange glamping tent set-up on site
• RSVP by 1 May 2018 to Kate at kate.anne.telford@mailbox-demo.com or Mark at mtelford@vantor-telford.com.au
• Will add extra information on event at later stage- see below for editable section.
Nice to have
• Editable section to add details, preferable at bottom of poster.

```html
<!DOCTYPE html>
<html lang="en">
<head>
<meta charset="utf-8">
<title>Brellafest – Mark Telford's 40th Festival</title>
<link rel="stylesheet" href="https://fonts.googleapis.com/css2?family=Open+Sans:ital,wght@0,300;0,400;0,600;1,400&family=Arimo:ital,wght@0,400;1,400&family=Courgette&family=Kalam:wght@300&display=swap">
<style>
  :root {
    --page-bg: #c9d3d4;
    --poster-black: #050405;
    --frame-line: rgba(255,255,255,0.85);
    --gold: #f2a814;
    --white: #ffffff;
    --headline-grey: #dcdcdc;
    --alert-red: #ee1111;
    --band-dark: rgba(30,24,20,0.82);
  }
  * { margin: 0; padding: 0; box-sizing: border-box; }
  html, body { width: 1200px; height: 1162px; overflow: hidden; }
  body { background: var(--page-bg); position: relative; }

  .poster {
    position: absolute; left: 235px; top: 31px;
    width: 730px; height: 1100px;
    background: var(--poster-black);
    overflow: hidden;
    color: var(--white);
    text-align: center;
  }
  .poster__swoosh {
    position: absolute; left: 0; top: 0; width: 730px; height: 240px;
    background:
      radial-gradient(ellipse 260px 70px at 120px 40px, rgba(200,16,26,0.85), transparent 70%),
      radial-gradient(ellipse 300px 80px at 560px 150px, rgba(200,16,26,0.8), transparent 70%),
      radial-gradient(ellipse 200px 60px at 420px 30px, rgba(150,10,20,0.6), transparent 70%);
  }
  .poster__celebration {
    position: absolute; left: 0; top: 760px; width: 730px; height: 340px;
    background:
      radial-gradient(ellipse 420px 220px at 365px 250px, rgba(200,137,30,0.75), transparent 75%),
      radial-gradient(ellipse 120px 180px at 50px 130px, rgba(200,137,30,0.45), transparent 75%),
      radial-gradient(ellipse 120px 180px at 680px 130px, rgba(200,137,30,0.45), transparent 75%),
      linear-gradient(to bottom, transparent, rgba(90,50,10,0.6));
  }
  .poster__frame {
    position: absolute; left: 22px; top: 24px; right: 12px; bottom: 94px;
    border: 1.5px solid var(--frame-line);
  }

  .host-name {
    position: absolute; left: 140px; top: 68px;
    font: 400 32px "Open Sans", sans-serif;
    color: var(--gold);
  }
  .headline {
    position: absolute; left: 0; top: 136px; width: 730px;
    font: 300 76px/100px "Open Sans", sans-serif;
    color: var(--headline-grey);
    letter-spacing: 1px;
  }
  .headline-rule {
    position: absolute; left: 300px; top: 252px; width: 370px; height: 2px;
    background: var(--headline-grey);
  }
  .event-name {
    position: absolute; left: 486px; top: 268px;
    font: 600 36px "Open Sans", sans-serif;
    color: var(--gold);
  }

  .event-details {
    position: absolute; left: 0; top: 338px; width: 730px;
    font: 400 22px/36px "Arimo", sans-serif;
    font-variant: small-caps; letter-spacing: 0.5px;
  }
  .welcome {
    position: absolute; left: 0; top: 476px; width: 730px;
    font: 400 50px/70px "Courgette", cursive;
  }
  .tent-note {
    position: absolute; left: 0; top: 618px; width: 730px;
    font: 300 29px/36px "Kalam", cursive;
  }
  .weekend-note {
    position: absolute; left: 0; top: 712px; width: 730px;
    font: italic 400 30px/36px "Arimo", sans-serif;
    color: var(--alert-red);
  }

  .rsvp-band {
    position: absolute; left: 0; top: 1004px; width: 730px; height: 74px;
    background: var(--band-dark);
    font: 400 18px/25px "Open Sans", sans-serif;
    padding-top: 12px;
  }
</style>
</head>
<body>
  <main class="poster">
    <div class="poster__swoosh" role="img" aria-label="Flowing red light swooshes across the top"></div>
    <div class="poster__celebration" role="img" aria-label="Champagne glasses raised over golden bokeh sparkles"></div>
    <div class="poster__frame"></div>

    <p class="host-name">Mark Telford's</p>
    <h1 class="headline">40th FESTIVAL</h1>
    <div class="headline-rule"></div>
    <p class="event-name">Brellafest</p>

    <div class="event-details">
      <p>Event date- 5-7th October 2018.</p>
      <p>Main event 6th October 2018 from 3pm-late</p>
      <p>Address is 412 Stony Creek Lane, Marulan NSW</p>
    </div>

    <div class="welcome">
      <p>All welcome,</p>
      <p>including children</p>
    </div>

    <div class="tent-note">
      <p>Bring your own tent or let us know and</p>
      <p>we can arrange glamping tent set-up on site</p>
    </div>

    <div class="weekend-note">
      <p>Come anytime over the weekend-</p>
      <p>food, drinks and fun provided</p>
    </div>

    <div class="rsvp-band">
      <p>RSVP by 1 May 2018 to Kate at kate.anne.telford@mailbox-demo.com</p>
      <p>or Mark at mtelford@vantor-telford.com.au</p>
    </div>
  </main>
</body>
</html>
```